Hypnotherapy- past life regression-life between lives therapist needs a website

I need a website that is enticing and spiritual in its feeling. It needs to have a lot of beautiful nature pictures included. The theme is "Quiet Harbor Path- what might you find....Lessons Solutions Answers"
Because all of us have the answers to living our best life, they are in our subconcious. But not everyone is capable of accessing them. Hypnosis accesses the subconcious and helps to create new neural pathways in the brain which can create new behaviors and responses to situations.
Hypnosis can help with anxiety, pain relief, weight loss, smoking/vaping cessation, self confidence......anything about yourself that you want to change.
Exploration of past lives and life between lives can reveal things related to ones current life. For example, perhaps your fear of deep water is a result of drowning in a past life. Once this has been discovered, it can lead to changes in ones current life.
Almost any personal behavior one wants to change, can be helped through hypnotherapy.
I need a page for testimonials, a place for scheduling (I will have a link to my scheduling app) some information about hypnotherapy.
I am uploading my logo files. My business card will be using the black and gold style, but my website does not have to reflect that. It can be based on the caramel and deep green like full color logo. Earthy, calm colors.
I also like the mock up of my logo on the beach and there was one on a starry night sky that I also liked.
Target Market(s)
men and women ages 25-50
Industry/Entity Type
natural health and wellness, spirituality
Number of Pages Required
4 page
Requirements
Must have
- a page for testimonials, perhaps with a beautiful nature picture with each one, I will have approximately 6. A link to schedule a complimentary intro session, preferably on the first page
Should not have
- no swinging watches or other sterotyped hypnosis symbols

```html
<!DOCTYPE html>
<html lang="en">
<head>
<meta charset="utf-8">
<title>Quiet Harbor Path — Hypnotherapy</title>
<link rel="stylesheet" href="https://fonts.googleapis.com/css2?family=Jost:ital,wght@0,400;0,500;0,600;1,400&family=Montserrat:wght@600;700&display=swap">
<style>
:root{
  --olive:#7f7a55;
  --olive-dark:#6d6a4a;
  --caramel:#e0882a;
  --ink:#111;
  --text:#555;
  --mist:#f1f4f2;
  --card:#dedfdd;
  --field:#dfe0df;
  --white:#fff;
}
*{box-sizing:border-box;margin:0;padding:0}
html,body{width:1200px;height:3952px;overflow:hidden}
body{position:relative;background:var(--white);font-family:"Jost",sans-serif;color:var(--ink)}
.abs{position:absolute}
.btn{position:absolute;display:flex;align-items:center;justify-content:center;background:var(--caramel);color:var(--white);border-radius:20px;font:600 13px "Jost",sans-serif;text-transform:uppercase;letter-spacing:.2px}
.h2{position:absolute;font:700 36px "Montserrat",sans-serif;color:var(--ink);letter-spacing:.3px}

/* header */
.topbar{left:575px;top:0;width:625px;height:41px;background:var(--olive);border-radius:0 0 0 22px}
.topbar .phone{position:absolute;left:68px;top:9px;color:var(--white);font:500 19px "Jost",sans-serif;display:flex;align-items:center;gap:8px}
.topbar .dot{position:absolute;top:14px;width:13px;height:13px;border-radius:50%;background:var(--white)}
.brand{left:52px;top:30px;display:flex;align-items:center;gap:10px;color:var(--caramel);font:600 20px "Jost",sans-serif;width:160px;line-height:1.05}
.brand .mark{width:34px;height:34px;border-radius:50%;border:3px solid var(--caramel);flex:none}
.nav{top:74px;font:500 18px "Jost",sans-serif;color:var(--ink)}

/* hero */
.hero{left:0;top:123px;width:1200px;height:600px;background:linear-gradient(180deg,#c9a98a 0%,#e0c4a0 35%,#e9cba4 60%,#dcb88e 100%)}
.hero-title{left:67px;top:238px;font:700 51px/62px "Montserrat",sans-serif;color:#8a8457;letter-spacing:.3px}
.hero-sub{left:75px;top:378px;font:400 23px/25px "Jost",sans-serif;color:#2e2a24;width:520px}

/* about */
.about-bg{left:0;top:706px;width:1200px;height:510px;background:var(--mist)}
.about-photo{left:104px;top:762px;width:406px;height:406px;border-radius:50%;background:linear-gradient(180deg,#8fb0d4 0%,#c8d9ea 55%,#9a9a96 80%,#7c7b78 100%)}
.about-text{left:594px;font:400 17px/22px "Jost",sans-serif;color:var(--text);width:470px}

/* services */
.grid{left:100px;top:1370px;width:996px;height:560px;display:grid;grid-template-columns:repeat(4,249px);grid-template-rows:280px 280px}
.tile-img{width:100%;height:100%}
.tile-text{background:var(--olive);color:var(--white);text-align:center;padding:42px 18px 0}
.tile-text h3{font:600 27px "Montserrat",sans-serif;margin-bottom:10px}
.tile-text p{font:400 14px/17px "Jost",sans-serif}

/* booking */
.book-title{left:0;width:1105px;top:2212px;text-align:center;font:700 36px "Montserrat",sans-serif;color:var(--white)}
.form{left:311px;top:2311px;width:533px;height:440px;background:var(--white);border-radius:24px}
.field{position:absolute;background:var(--field);border-radius:18px;font:500 14px "Jost",sans-serif;color:#8a8a8a;padding:10px 20px}

/* testimonials */
.quote{top:2994px;width:305px;height:261px;background:var(--card);border-radius:14px;padding:38px 40px 0}
.quote p{font:italic 400 19px/25px "Jost",sans-serif;color:#888}
.quote .who{position:absolute;left:31px;top:196px;display:flex;align-items:center;gap:12px}
.quote .avatar{width:52px;height:52px;border-radius:50%;background:linear-gradient(160deg,#5a4a3a,#c9b8a8);border:3px solid #bcc6d8}
.quote .name{font:500 15px "Jost",sans-serif;color:var(--ink)}
.quote .role{font:400 8px "Jost",sans-serif;color:#888}
.dot-nav{top:3313px;width:19px;height:19px;border-radius:50%;background:var(--olive)}

/* footer */
.fnav{top:3660px;display:flex;align-items:center;gap:10px;color:var(--white);font:500 19px "Jost",sans-serif}
.fcontact{top:3752px;display:flex;align-items:center;gap:12px;color:var(--white);font:400 15px "Jost",sans-serif}
.fsocial{top:3818px;width:28px;height:28px;border-radius:50%;background:var(--white)}
.fine{top:3914px;color:var(--white);font:400 12px "Jost",sans-serif}
</style>
</head>
<body>

<!-- header -->
<div class="abs topbar">
  <div class="phone">
    <svg width="22" height="22" viewBox="0 0 24 24" fill="none" stroke="#fff" stroke-width="1.8"><path d="M5 3h4l2 5-3 2a12 12 0 0 0 6 6l2-3 5 2v4a2 2 0 0 1-2 2A18 18 0 0 1 3 5a2 2 0 0 1 2-2z"/></svg>
    1122-555-0199
  </div>
  <span class="dot" style="left:413px"></span>
  <span class="dot" style="left:453px"></span>
  <span class="dot" style="left:493px"></span>
</div>
<div class="abs brand"><span class="mark"></span><span>Quiet Harbor Path</span></div>
<div class="abs nav" style="left:324px">Home</div>
<div class="abs nav" style="left:410px">About Us</div>
<div class="abs nav" style="left:516px">Services</div>
<div class="abs nav" style="left:618px">Testimonials</div>
<div class="abs nav" style="left:766px">Contact</div>
<div class="btn" style="left:884px;top:68px;width:207px;height:37px">Schedule a Session</div>

<!-- hero -->
<div class="abs hero" role="img" aria-label="Wooden arched doorway standing in a sunlit desert of rippled sand"></div>
<svg class="abs" style="left:0;top:560px" width="1200" height="170" viewBox="0 0 1200 170">
  <path d="M0 50 C300 130 600 160 820 140 C1000 124 1120 90 1200 52 L1200 170 L0 170Z" fill="#7f7a55"/>
  <path d="M0 82 C300 150 600 168 820 150 C1000 136 1120 104 1200 72 L1200 170 L0 170Z" fill="#f1f4f2"/>
</svg>
<div class="abs hero-title">QUIET HARBOR PATH<br>WHAT MIGHT YOU FIND</div>
<div class="abs hero-sub">Exploration of past lives and life between lives can reveal things related to ones current life.</div>
<div class="btn" style="left:75px;top:473px;width:160px;height:36px">Get a Quote</div>

<!-- about -->
<div class="abs about-bg"></div>
<div class="abs about-photo" role="img" aria-label="Man in a suit climbing stone steps toward a bright cloudy sky"></div>
<div class="h2" style="left:594px;top:824px">ABOUT US</div>
<p class="abs about-text" style="top:884px">Lorem ipsum dolor sit amet, consectetur adipiscing elit, sed do eiusmod tempor incididunt ut labore et dolore magna aliqua. Ut enim ad minim veniam, quis nostrud exercitation ullamco laboris nisi ut aliquip ex ea commodo consequat.</p>
<p class="abs about-text" style="top:992px">Duis aute irure dolor in reprehenderit in voluptate velit esse cillum dolore eu fugiat nulla pariatur. Excepteur sint occaecat cupidatat non proident, sunt in culpa qui officia deserunt mollit anim id est laborum.</p>
<div class="btn" style="left:594px;top:1103px;width:160px;height:37px">Get a Quote</div>

<!-- services -->
<div class="h2" style="left:0;width:1165px;top:1296px;text-align:center">OUR SERVICES</div>
<div class="abs grid">
  <div class="tile-img" role="img" aria-label="Therapist supporting a woman's arm during a session" style="background:linear-gradient(160deg,#e8e6e0,#5a63a8 60%,#8a9a6a)"></div>
  <div class="tile-text"><h3>Anxiety</h3><p>Lorem ipsum dolor sit amet, consectetur adipiscing elit, sed do eiusmod tempor incididunt ut labore et dolore magna aliqua. Ut enim ad minim veniam, quis nostrud exercitation ullamco laboris nisi ut aliquip ex ea commodo consequat.</p></div>
  <div class="tile-img" role="img" aria-label="Woman holding her lower back in pain" style="background:linear-gradient(160deg,#d8d4cc,#b89a84 50%,#ece8e2)"></div>
  <div class="tile-text"><h3>Pain Relief</h3><p>Lorem ipsum dolor sit amet, consectetur adipiscing elit, sed do eiusmod tempor incididunt ut labore et dolore magna aliqua. Ut enim ad minim veniam, quis nostrud exercitation ullamco laboris nisi ut aliquip ex ea commodo consequat.</p></div>
  <div class="tile-text"><h3>Weight Loss</h3><p>Lorem ipsum dolor sit amet, consectetur adipiscing elit, sed do eiusmod tempor incididunt ut labore et dolore magna aliqua. Ut enim ad minim veniam, quis nostrud exercitation ullamco laboris nisi ut aliquip ex ea commodo consequat.</p></div>
  <div class="tile-img" role="img" aria-label="Green apple and measuring tape held at the waist" style="background:linear-gradient(180deg,#2a2a2a 0%,#d9b8a4 35%,#a8c04a 55%,#d9b8a4 75%,#2a2a2a 100%)"></div>
  <div class="tile-text"><h3>Self Confidence</h3><p>Lorem ipsum dolor sit amet, consectetur adipiscing elit, sed do eiusmod tempor incididunt ut labore et dolore magna aliqua. Ut enim ad minim veniam, quis nostrud exercitation ullamco laboris nisi ut aliquip ex ea commodo consequat.</p></div>
  <div class="tile-img" role="img" aria-label="Man with open arms facing a misty mountain view" style="background:linear-gradient(160deg,#eeeeec,#c8c8c4 50%,#3a3a38 80%,#8a8680)"></div>
</div>
<div class="btn" style="left:514px;top:1980px;width:160px;height:37px">View All Services</div>

<!-- booking -->
<svg class="abs" style="left:0;top:2130px" width="1200" height="680" viewBox="0 0 1200 680" role="img" aria-label="Softly lit doorway in a muted olive room">
  <defs><linearGradient id="bookTone" x1="0" x2="1"><stop offset="0" stop-color="#6f6c4c"/><stop offset=".5" stop-color="#7d7856"/><stop offset="1" stop-color="#6f6c4c"/></linearGradient></defs>
  <ellipse cx="600" cy="339" rx="900" ry="339" fill="url(#bookTone)"/>
</svg>
<div class="abs book-title">BOOK THE SERVICES</div>
<div class="abs form">
  <div class="field" style="left:47px;top:46px;width:440px;height:37px">Name</div>
  <div class="field" style="left:47px;top:112px;width:440px;height:37px">Email</div>
  <div class="field" style="left:49px;top:176px;width:440px;height:37px">Subject</div>
  <div class="field" style="left:51px;top:241px;width:440px;height:133px;border-radius:26px;padding-top:20px">Message</div>
  <div class="btn" style="left:186px;top:393px;width:161px;height:37px">Submit Now</div>
</div>

<!-- testimonials -->
<div class="h2" style="left:0;width:1160px;top:2870px;text-align:center">WHAT CLIENT SAYS</div>
<div class="abs quote" style="left:95px"><p>Lorem ipsum dolor sit amet, consectetur adipiscingelit, sed do eiusmod tempor incididunt ut laboreet dolore magna aliqua.</p><div class="who"><div class="avatar"></div><div><div class="name">Mara Lind</div><div class="role">Housewife</div></div></div></div>
<div class="abs quote" style="left:445px"><p>Lorem ipsum dolor sit amet, consectetur adipiscingelit, sed do eiusmod tempor incididunt ut laboreet dolore magna aliqua.</p><div class="who"><div class="avatar"></div><div><div class="name">Mara Lind</div><div class="role">Housewife</div></div></div></div>
<div class="abs quote" style="left:795px"><p>Lorem ipsum dolor sit amet, consectetur adipiscingelit, sed do eiusmod tempor incididunt ut laboreet dolore magna aliqua.</p><div class="who"><div class="avatar"></div><div><div class="name">Mara Lind</div><div class="role">Housewife</div></div></div></div>
<div class="abs dot-nav" style="left:543px"></div>
<div class="abs dot-nav" style="left:586px;background:transparent;border:2px solid var(--olive)"></div>
<div class="abs dot-nav" style="left:629px"></div>

<!-- footer -->
<svg class="abs" style="left:0;top:3400px" width="1200" height="552" viewBox="0 0 1200 552">
  <path d="M0 110 C300 40 700 10 1200 55 L1200 552 L0 552Z" fill="#7f7a55"/>
  <path d="M0 122 C300 72 700 46 1200 100 L1200 552 L0 552Z" fill="#000"/>
</svg>
<div class="abs brand" style="left:141px;top:3680px;width:170px;color:var(--caramel)"><span class="mark"></span><span>Quiet Harbor Path</span></div>

<svg width="0" height="0" style="position:absolute"><defs>
  <symbol id="go" viewBox="0 0 20 20"><circle cx="10" cy="10" r="8" fill="none" stroke="#e0882a" stroke-width="1.8"/><path d="M6 10h7M10 7l3 3-3 3" fill="none" stroke="#e0882a" stroke-width="1.8"/></symbol>
</defs></svg>
<div class="abs fnav" style="left:384px"><svg width="19" height="19"><use href="#go"/></svg>Home</div>
<div class="abs fnav" style="left:506px"><svg width="19" height="19"><use href="#go"/></svg>About</div>
<div class="abs fnav" style="left:631px;top:3663px"><svg width="19" height="19"><use href="#go"/></svg>Services</div>
<div class="abs fnav" style="left:786px;top:3663px"><svg width="19" height="19"><use href="#go"/></svg>Blog</div>
<div class="abs fnav" style="left:918px;top:3664px"><svg width="19" height="19"><use href="#go"/></svg>Contact</div>
<div class="abs" style="left:384px;top:3712px;width:634px;height:2px;background:#c9c9c9"></div>

<div class="abs fcontact" style="left:388px"><svg width="20" height="20" viewBox="0 0 24 24" fill="#e0882a"><path d="M5 2h4l2 5-3 2a12 12 0 0 0 6 6l2-3 5 2v4a2 2 0 0 1-2 2A18 18 0 0 1 3 4a2 2 0 0 1 2-2z"/></svg>(+62)555 010 482</div>
<div class="abs fcontact" style="left:600px;top:3750px"><svg width="22" height="18" viewBox="0 0 22 18"><rect x="1" y="4" width="20" height="13" rx="2" fill="#e0882a"/><path d="M1 5l10 7 10-7" fill="none" stroke="#000" stroke-width="1.5"/></svg>hello@harborpath.example</div>
<div class="abs fcontact" style="left:833px"><svg width="18" height="22" viewBox="0 0 18 22"><path d="M9 1a7 7 0 0 1 7 7c0 5-7 13-7 13S2 13 2 8a7 7 0 0 1 7-7z" fill="#e0882a"/><circle cx="9" cy="8" r="2.6" fill="#000"/></svg>Jl. Teluk Senja No.12, Tenang</div>

<span class="abs fsocial" style="left:134px"></span>
<span class="abs fsocial" style="left:205px"></span>
<span class="abs fsocial" style="left:280px"></span>

<div class="abs fine" style="left:135px">Copyright 2023, All Rights Reserved.</div>
<div class="abs fine" style="left:815px;top:3920px">Privacy Policy | Term and Conditions</div>

</body>
</html>
```